Plakat-Design für Graf Nebel
Zielgruppe
Musiker. Politischer Liedermacher. Kabarett.
Aufgabenstellung
Konzertplakat
Text:
Graf Nebel
Live!
Schriftzug Graf Nebel muss sehr gut lesbar sein, auch vom Auto aus.
Design für Plakate in A1 und A3.
Die Fotovorlage ist leider noch nicht optimal (Gesichtsfarbe usw.)
Sollte nachbeabeitet werden.
Unten weißen Balken freilassen für die Informationen der jeweiligen Veranstalter

```html
<!DOCTYPE html>
<html lang="de">
<head>
<meta charset="utf-8">
<title>Graf Nebel – Live! Konzertplakat</title>
<link rel="stylesheet" href="https://fonts.googleapis.com/css2?family=Archivo+Black&family=Permanent+Marker&display=swap">
<style>
  :root {
    --stage-black: #050505;
    --stage-grey: #2a2a2a;
    --ink-white: #ffffff;
    --ink-black: #000000;
    --signal-red: #c9161d;
    --jacket-red: #d8343a;
    --wood-light: #e7d3a8;
    --wood-dark: #8a5a34;
  }
  * { margin: 0; padding: 0; box-sizing: border-box; }
  html, body {
    width: 849px; height: 1200px; overflow: hidden;
    background: var(--ink-white);
  }
  .poster {
    position: relative; width: 849px; height: 1200px; overflow: hidden;
    background: var(--ink-white);
  }
  .stage {
    position: absolute; left: 0; top: 0; width: 849px; height: 1003px;
    background: radial-gradient(ellipse at 20% 30%, var(--stage-grey) 0%, var(--stage-black) 60%);
  }
  .artist-photo {
    position: absolute; left: 293px; top: 183px; width: 556px; height: 820px;
    background:
      radial-gradient(ellipse at 82% 22%, #c99a7e 0%, rgba(201,154,126,0) 18%),
      radial-gradient(ellipse at 45% 70%, var(--wood-light) 0%, rgba(231,211,168,0) 38%),
      linear-gradient(160deg, var(--wood-dark) 0%, var(--jacket-red) 55%, #f2f0ec 100%);
    border-radius: 260px 0 0 0;
    opacity: 0.95;
  }
  .artist-name {
    position: absolute; left: 57px; top: 92px;
    font-family: "Archivo Black", "Arial Black", sans-serif;
    color: var(--ink-white); text-transform: uppercase; line-height: 0.92;
    letter-spacing: 2px;
  }
  .artist-name .first { display: block; font-size: 88px; }
  .artist-name .last { display: block; font-size: 132px; margin-left: 40px; }
  .live-mark {
    position: absolute; left: 50px; top: 600px;
    font-family: "Permanent Marker", cursive;
    font-size: 170px; line-height: 1; color: var(--signal-red);
    transform: rotate(-6deg); transform-origin: left bottom;
  }
  .info-band {
    position: absolute; left: 0; top: 1003px; width: 849px; height: 197px;
  }
  .info-band svg { display: block; }
  .date { font-family: "Archivo Black", "Arial Black", sans-serif; fill: var(--ink-black); }
  .venue { font-family: "Archivo Black", "Arial Black", sans-serif; fill: var(--ink-black); }
  .note { font-family: "Archivo Black", "Arial Black", sans-serif; fill: var(--signal-red); }
</style>
</head>
<body>
<main class="poster">
  <div class="stage" role="img" aria-label="Dunkler Hintergrund mit schemenhaften Mandolinen und Gitarren"></div>
  <div class="artist-photo" role="img" aria-label="Foto des Liedermachers in roter Jacke mit Mandoline und Gitarren"></div>

  <h1 class="artist-name">
    <span class="first">Graf</span>
    <span class="last">Nebel</span>
  </h1>

  <p class="live-mark">Live!</p>

  <section class="info-band">
    <svg width="849" height="197" viewBox="0 0 849 197">
      <text class="date" x="37" y="84" font-size="92" textLength="770" lengthAdjust="spacingAndGlyphs">xx. Januar 2018</text>
      <text class="venue" x="37" y="134" font-size="31" textLength="504" lengthAdjust="spacingAndGlyphs">Musterhalle Musterheim</text>
      <text class="venue" x="578" y="134" font-size="25" textLength="230" lengthAdjust="spacingAndGlyphs">Einlass 19 Uhr</text>
      <text class="note" x="37" y="183" font-size="34" textLength="775" lengthAdjust="spacingAndGlyphs">Mustertext lorem ipusem quid soluse</text>
    </svg>
  </section>
</main>
</body>
</html>
```